Need Website for PR Firm

I need a website for my new business, Harbinger Press Collective, a PR, Communications and Marketing Firm. I want something classy and clean. Tailored and professional with a bit of a whimsical touch. Colors are mainly white and green. I don't like random stock photos but I would consider an image of a park with the city in the background. The name of my company is a play on Willowmere Commons in Brooklyn where I am based.

The navigation and pages I will need is a good clean landing page.
About us
Who we are
Contact

Again, I like clean white and the copy in a similar color and font as my logo.
No stock photography or clip art.
I uploaded an image of the park that I like and wld be open to using in some way
Updates

I have uploaded an image of the park that you could implemented. 

Seeing some good designs here.

With the image I uploaded, I unfortunately think the green sky is too green.
Wondering if we can make modifications to the color of the sky.
I like the last image submitted too.

Target Market(s)

Professionals and the media who are seeing how I represent myself and my agency as they hire me for the public relations council.

Industry/Entity Type

Business

Font styles to use
Serif
Other font styles liked:
• Trajan

Colors
acd036
ffffff
dbdbdb
eeeeee

Requirements
Must have
• High quality and consistent colors and font.
Should not have
• Stock photography
Clip art
colors that aren't white, the green in my font, black or gray if necessary.

```html
<!DOCTYPE html>
<html lang="en">
<head>
<meta charset="utf-8">
<title>Harbinger Press Collective</title>
<link rel="stylesheet" href="https://fonts.googleapis.com/css2?family=Cinzel:wght@400&display=swap">
<style>
  :root {
    --sky: #c8e3e3;
    --brand-green: #8aae12;
    --ink: #4f5b5b;
    --white: #ffffff;
    --ground: #dbdbdb;
    --leaf: #8aa868;
  }
  html, body {
    margin: 0;
    padding: 0;
    overflow: hidden;
  }
  body {
    width: 1200px;
    height: 680px;
    background: var(--sky);
    position: relative;
    font-family: "Cinzel", serif;
  }
  .brand {
    position: absolute;
    left: 104px;
    top: 38px;
    margin: 0;
    color: var(--brand-green);
    font-weight: 400;
    font-size: 27px;
    line-height: 27px;
    letter-spacing: 0.5px;
  }
  .brand span { display: block; }
  .site-nav {
    position: absolute;
    left: 1034px;
    top: 36px;
  }
  .site-nav ul {
    list-style: none;
    margin: 0;
    padding: 0;
  }
  .site-nav a {
    display: block;
    color: var(--white);
    text-decoration: none;
    font-size: 20px;
    line-height: 31.5px;
    letter-spacing: 1.2px;
  }
  .site-nav a.is-current { color: var(--brand-green); }
  .intro {
    position: absolute;
    left: 258px;
    top: 214px;
    width: 720px;
    margin: 0;
    color: var(--ink);
    font-size: 29px;
    line-height: 40px;
    letter-spacing: 0.8px;
    font-weight: 400;
  }
  .park-scene {
    position: absolute;
    left: 0;
    top: 430px;
    width: 1200px;
    height: 196px;
    background: linear-gradient(to bottom, var(--sky) 0%, var(--leaf) 55%, var(--ground) 100%);
  }
  .site-footer {
    position: absolute;
    left: 0;
    top: 626px;
    width: 1200px;
    height: 54px;
    background: var(--brand-green);
  }
  .copyright {
    position: absolute;
    left: 30px;
    top: 20px;
    margin: 0;
    color: var(--white);
    font-family: Arial, Helvetica, sans-serif;
    font-weight: 700;
    font-size: 10px;
  }
  .social {
    position: absolute;
    right: 29px;
    top: 16px;
    display: flex;
    gap: 6px;
    list-style: none;
    margin: 0;
    padding: 0;
  }
  .social li {
    width: 22px;
    height: 22px;
    background: var(--white);
  }
</style>
</head>
<body>
  <header>
    <h1 class="brand"><span>Harbinger</span><span>Press</span><span>Collective</span></h1>
    <nav class="site-nav">
      <ul>
        <li><a class="is-current" href="#">Home</a></li>
        <li><a href="#">about us</a></li>
        <li><a href="#">who we are</a></li>
        <li><a href="#">contact</a></li>
      </ul>
    </nav>
  </header>

  <main>
    <p class="intro">Nullam quis risus eget urna mollis ornare vel eu leo. Cum sociis natoque penatibus et magnis dis parturient montes, nascetur.</p>
    <div class="park-scene" role="img" aria-label="Illustration of Willowmere Commons: a stone arch at the end of a tree-lined promenade with people strolling"></div>
  </main>

  <footer class="site-footer">
    <p class="copyright">Copyright ©2014 Harbinger Press Collective</p>
    <ul class="social" aria-label="Social links">
      <li></li>
      <li></li>
      <li></li>
    </ul>
  </footer>
</body>
</html>
```